Honey apple cider vinegar label

organic food company need a contemporary honey apple cider vinegar and honey vinegar label, natural GMP logo HACCP LOgo
label detail height :140mm Width:80mm
ingredient: honey, apple cider vinegar and water, free from artificial color & preservative
Shelf Life: 3 years
Net weight 400ml
Storage : store in cool place , do not expose to sunlight
instruction for use: add 20ml to a full glass of water 3, times a days before meal, stop consuming if allergies happen
certification, GMP HACCP, Halal, natural product

Target Market(s)

health conscious group

Requirements
Must have
• modern feel, honey and apple picture

```html
<!DOCTYPE html>
<html lang="en">
<head>
<meta charset="utf-8">
<title>Honey Apple Cider Vinegar Labels</title>
<link href="https://fonts.googleapis.com/css2?family=Merriweather:wght@400;700&family=Open+Sans:wght@400;600;700;800&display=swap" rel="stylesheet">
<style>
  :root {
    --band: #2d1b3d;
    --green: #5f9a3b;
    --ink: #3a3a3a;
    --paper: #ffffff;
    --honey: #f1b52a;
    --apple: #b3222c;
    --seal: #b9c7e0;
  }
  * { margin: 0; padding: 0; box-sizing: border-box; }
  html, body { width: 1200px; height: 1051px; overflow: hidden; background: var(--paper); }
  .sheet { position: relative; width: 1200px; height: 1051px; display: flex; gap: 4px; }
  .label { position: relative; width: 598px; height: 1051px; background: var(--paper); overflow: hidden; }
  .band { position: absolute; left: 0; right: 0; height: 17px; background: var(--band); }
  .band--top { top: 0; }
  .band--bottom { bottom: 0; height: 19px; }

  .brand { position: absolute; top: 34px; left: 0; right: 0; text-align: center; }
  .brand__dot { display: block; width: 38px; height: 38px; margin: 0 auto 8px; border-radius: 50%; background: var(--honey); }
  .brand__name { font-family: "Open Sans", sans-serif; font-weight: 700; font-size: 25px; color: var(--band); letter-spacing: 0.5px; }

  .title { position: absolute; left: 0; right: 0; text-align: center; font-family: "Merriweather", serif; color: var(--green); line-height: 1; white-space: nowrap; }
  .title--bold { top: 146px; font-weight: 700; }
  .title--bold .title__line1 { display: block; font-size: 90px; letter-spacing: -1px; }
  .title--bold .title__line2 { display: block; font-size: 75px; margin-top: 5px; letter-spacing: -0.5px; }
  .title--light { top: 154px; font-weight: 400; }
  .title--light .title__line1 { display: block; font-size: 62px; letter-spacing: -0.5px; }
  .title--light .title__line2 { display: block; font-size: 116px; margin-top: -12px; letter-spacing: 1px; }

  .hero { position: absolute; left: 40px; top: 360px; width: 520px; height: 515px; }

  .ingredients { position: absolute; left: 33px; right: 20px; top: 889px; font-family: "Open Sans", sans-serif; font-size: 20.5px; line-height: 1.05; color: var(--ink); }
  .ingredients strong { font-weight: 700; }

  .shelf { position: absolute; left: 10px; top: 975px; font-family: "Open Sans", sans-serif; font-weight: 700; font-size: 14px; line-height: 1.45; color: var(--ink); }
  .seals { position: absolute; left: 159px; top: 961px; display: flex; gap: 28px; align-items: center; }
  .seal { width: 58px; height: 58px; border-radius: 50%; background: var(--seal); }
  .seal--halal { background: var(--green); opacity: 0.8; }
  .seal--gmp { background: var(--green); }
  .volume { position: absolute; right: 12px; top: 983px; font-family: "Open Sans", sans-serif; font-weight: 800; font-size: 27px; color: var(--ink); }
</style>
</head>
<body>
<main class="sheet">
  <section class="label label--bold">
    <div class="band band--top"></div>
    <div class="brand"><span class="brand__dot"></span><span class="brand__name">orchardia</span></div>
    <h1 class="title title--bold"><span class="title__line1">Honey Apple</span><span class="title__line2">Cider VINEGER</span></h1>
    <svg class="hero" viewBox="0 0 520 515" role="img" aria-label="Illustration of a honey jar with honeycomb, red and green apples with splashes, and a 100% natural product badge">
      <defs>
        <radialGradient id="heroHoneyA" cx="32%" cy="50%" r="50%">
          <stop offset="0" stop-color="#f4bd3a"/>
          <stop offset="0.6" stop-color="#eaa52a" stop-opacity="0.8"/>
          <stop offset="1" stop-color="#ffffff" stop-opacity="0"/>
        </radialGradient>
        <radialGradient id="heroAppleA" cx="68%" cy="45%" r="42%">
          <stop offset="0" stop-color="#b3222c" stop-opacity="0.85"/>
          <stop offset="0.7" stop-color="#a31e2a" stop-opacity="0.5"/>
          <stop offset="1" stop-color="#ffffff" stop-opacity="0"/>
        </radialGradient>
      </defs>
      <rect width="520" height="515" fill="url(#heroHoneyA)"/>
      <rect width="520" height="515" fill="url(#heroAppleA)"/>
    </svg>
    <p class="ingredients"><strong>Ingredient:</strong> honey, apple cider vinegar and water, free from artificial color &amp; preservative</p>
    <p class="shelf">Shelf Life:<br>3 years</p>
    <div class="seals"><span class="seal"></span><span class="seal seal--halal"></span><span class="seal seal--gmp"></span></div>
    <p class="volume">400ml</p>
    <div class="band band--bottom"></div>
  </section>

  <section class="label label--light">
    <div class="band band--top"></div>
    <div class="brand"><span class="brand__dot"></span><span class="brand__name">orchardia</span></div>
    <h1 class="title title--light"><span class="title__line1">Honey Apple Cider</span><span class="title__line2">VINEGER</span></h1>
    <svg class="hero" viewBox="0 0 520 515" role="img" aria-label="Illustration of a honey jar with honeycomb, red and green apples with splashes, and a 100% natural product badge">
      <defs>
        <radialGradient id="heroHoneyB" cx="32%" cy="50%" r="50%">
          <stop offset="0" stop-color="#f4bd3a"/>
          <stop offset="0.6" stop-color="#eaa52a" stop-opacity="0.8"/>
          <stop offset="1" stop-color="#ffffff" stop-opacity="0"/>
        </radialGradient>
        <radialGradient id="heroAppleB" cx="68%" cy="45%" r="42%">
          <stop offset="0" stop-color="#b3222c" stop-opacity="0.85"/>
          <stop offset="0.7" stop-color="#a31e2a" stop-opacity="0.5"/>
          <stop offset="1" stop-color="#ffffff" stop-opacity="0"/>
        </radialGradient>
      </defs>
      <rect width="520" height="515" fill="url(#heroHoneyB)"/>
      <rect width="520" height="515" fill="url(#heroAppleB)"/>
    </svg>
    <p class="ingredients"><strong>Ingredient:</strong> honey, apple cider vinegar and water, free from artificial color &amp; preservative</p>
    <p class="shelf">Shelf Life:<br>3 years</p>
    <div class="seals"><span class="seal"></span><span class="seal seal--halal"></span><span class="seal seal--gmp"></span></div>
    <p class="volume">400ml</p>
    <div class="band band--bottom"></div>
  </section>
</main>
</body>
</html>
```